" Escritório de advocacia com expertise em direito de familias e sucessões mas atende também outras áreas como condomínios, pensão e trabalhistas. Acreditamos na atuação preventiva do advogado, evitando crises, minimizando impacto de problemas, Visão holística da demanda para formulação de estratégia e foto nas possibilidade de resolução de litígio. Mediação. "

```html
<!DOCTYPE html>
<html lang="pt-BR">
<head>
<meta charset="utf-8">
<title>Pasta Institucional – Marina Duarte Advocacia</title>
<link rel="stylesheet" href="https://fonts.googleapis.com/css2?family=Montserrat:wght@300;400&display=swap">
<style>
  :root {
    --page-bg: #ffffff;
    --folder-face: #333333;
    --folder-flap: #383838;
    --fold-line: #2b2b2b;
    --gold: #c9a36a;
    --ink-light: #e6e6e6;
    --ink-muted: #b5b5b5;
  }
  html, body {
    margin: 0;
    padding: 0;
    width: 1200px;
    height: 1200px;
    overflow: hidden;
    background: var(--page-bg);
  }
  .canvas {
    display: block;
    width: 1200px;
    height: 1200px;
  }
  .folder-face { fill: var(--folder-face); }
  .pocket-flap { fill: var(--folder-flap); }
  .fold-line { stroke: var(--fold-line); stroke-width: 2; }
  .gold-frame { fill: none; stroke: var(--gold); stroke-width: 2; }
  .brand-name {
    font-family: "Montserrat", sans-serif;
    font-weight: 300;
    letter-spacing: 3px;
  }
  .brand-name--cover { fill: var(--gold); font-size: 22px; }
  .brand-name--back { fill: var(--ink-light); font-size: 14px; letter-spacing: 2px; }
  .brand-sub {
    font-family: "Montserrat", sans-serif;
    font-weight: 300;
    font-size: 8px;
    letter-spacing: 6px;
  }
  .brand-sub--cover { fill: var(--gold); }
  .brand-sub--back { fill: var(--ink-light); font-size: 6px; letter-spacing: 4px; }
  .contact-line {
    font-family: "Montserrat", sans-serif;
    font-weight: 300;
    font-size: 13px;
    fill: var(--ink-light);
  }
  .address-line {
    font-family: "Montserrat", sans-serif;
    font-weight: 300;
    font-size: 8.5px;
    fill: var(--ink-muted);
  }
</style>
</head>
<body>
<svg class="canvas" viewBox="0 0 1200 1200" xmlns="http://www.w3.org/2000/svg">
  <!-- pocket flap -->
  <path class="pocket-flap"
        d="M113 780 L82 800 L79 1035 L113 1068 L360 1068
           C480 1068 619 1000 619 857 L113 857 Z"/>

  <!-- folder body -->
  <rect class="folder-face" x="113" y="144" width="1008" height="713"/>
  <line class="fold-line" x1="619" y1="144" x2="619" y2="857"/>

  <!-- gold frame -->
  <rect class="gold-frame" x="139" y="170" width="953" height="656"/>

  <!-- cover brand -->
  <g class="cover-brand">
    <text class="brand-name brand-name--cover" x="857" y="500" text-anchor="middle">MARINA DUARTE</text>
    <text class="brand-sub brand-sub--cover" x="857" y="516" text-anchor="middle">ADVOCACIA</text>
  </g>

  <!-- back panel brand and contacts -->
  <g class="back-brand">
    <text class="brand-name brand-name--back" x="382" y="756" text-anchor="middle">MARINA DUARTE</text>
    <text class="brand-sub brand-sub--back" x="382" y="766" text-anchor="middle">ADVOCACIA</text>
  </g>
  <g class="contacts">
    <text class="contact-line" x="382" y="790" text-anchor="middle">(62) 3000-1234 · contato@marinaduarte.adv.br · www.marinaduarte.adv.br</text>
    <text class="address-line" x="382" y="808" text-anchor="middle">Avenida Central nº 100 - sala 12 - Setor Sul Ed. Horizonte - CEP 74.000-000 - Goiânia - GO</text>
  </g>
</svg>
</body>
</html>
```